Rise As Captain Book Cover Design

Book Cover Design Brief
Book Title
Rise As Captain
Subtitle
The 10 Quiet Habits of Remarkable Command
Author
Orwen Dalquist
Overview
This book is about leadership that starts within.
Most leadership books focus on tactics or management strategies. This book focuses on the inner disciplines that create powerful leaders — mindset, integrity, focus, empathy, professionalism, honesty, and self-respect.
The tone of the book is bold, direct, confident, and transformational.
This is not a soft or corporate leadership book. It is a call to step up and become the leader you are capable of becoming.
The cover should feel:
• Powerful
• Professional
• Transformational
• Premium
• Memorable
Think best-selling leadership book, not a generic business book.
Target Audience
Business owners
Managers
Entrepreneurs
Team leaders
Professionals who want to grow as leaders
Most readers are ambitious professionals who want to level up their leadership and life.
Design Direction
The design should communicate:
Strength. Discipline. Leadership. Personal transformation.
Avoid cliché leadership visuals like:
• Handshakes
• Office buildings
• Corporate stock imagery
• Teams sitting around tables
The design should feel iconic, bold, and timeless.
Think about covers of successful leadership books such as:
Copper Rituals
Total Stewardship
Won't Break Now
Begin From Purpose
The 36 Rules of Sway
These covers are simple, powerful, and recognizable even at small sizes.
Typography
The title RISE AS CAPTAIN should be:
• Bold
• Strong
• Dominant on the cover
• Easy to read even at small sizes (important for Vellora thumbnails)
The subtitle should be clean and secondary to the title.
The overall typography should feel strong, modern, and premium.
Color Direction
Designers are free to explore colors, but the cover should feel strong and premium, not playful.
Colors that often work well for leadership books include:
Black
Gold
White
Deep blue
Dark red
High contrast and clarity are important.
Style
Preferred style:
• Clean
• Modern
• Minimal
• Strong contrast
Avoid clutter and overly busy designs.
The goal is to create a cover that feels powerful and professional at first glance.
Deliverables
Front cover design for a leadership book.
Final files should include:
• High resolution artwork
• Editable source files
• Print-ready version suitable for publishing
Goal of the Cover
When someone sees this book on Vellora or in a bookstore, they should immediately think:
“This looks like a serious leadership book.”
The design should feel like it belongs next to books by authors such as:
Marcus Thorley
Brandt Osgood
Peter Hollis
Nolan Fairbrook
A strong, confident cover that attracts leaders who want to grow and perform at a higher level.
Target Market(s)
Business Owners and High level managers
Look and feel
Each slider illustrates characteristics of the customer's brand and the style your logo design should communicate.

```html
<!DOCTYPE html>
<html lang="en">
<head>
<meta charset="utf-8">
<title>Rise As Captain — Book Cover</title>
<link rel="stylesheet" href="https://fonts.googleapis.com/css2?family=Cabin+Condensed:wght@700&family=Cabin:wght@700&display=swap">
<style>
  :root {
    --cover-teal: #04586f;
    --ink-white: #ffffff;
    --gold-light: #f9d59a;
    --gold-mid: #f9df7a;
    --gold-deep: #a55e22;
    --gold-numeral: #f7d79c;
  }
  html, body {
    margin: 0;
    padding: 0;
    overflow: hidden;
    background: var(--cover-teal);
  }
  .cover {
    position: relative;
    width: 927px;
    height: 1200px;
    background: var(--cover-teal);
    overflow: hidden;
  }
  .cover__author {
    position: absolute;
    top: 40px;
    left: 0;
    width: 100%;
    margin: 0;
    text-align: center;
    font-family: "Cabin", sans-serif;
    font-weight: 700;
    font-size: 62px;
    letter-spacing: 1px;
    font-variant: small-caps;
    color: var(--ink-white);
    line-height: 1;
  }
  .cover__title {
    position: absolute;
    inset: 0;
    width: 927px;
    height: 1200px;
  }
  .cover__title text {
    font-family: "Cabin Condensed", sans-serif;
    font-weight: 700;
  }
  .cover__subtitle {
    position: absolute;
    top: 1012px;
    left: 0;
    width: 100%;
    margin: 0;
    text-align: center;
    font-family: "Cabin", sans-serif;
    font-weight: 700;
    font-size: 34px;
    line-height: 47px;
    color: var(--ink-white);
  }
  .cover__numeral {
    color: var(--gold-numeral);
    font-size: 48px;
    vertical-align: -3px;
  }
</style>
</head>
<body>
<main class="cover">
  <p class="cover__author">Orwen Dalquist</p>

  <svg class="cover__title" viewBox="0 0 927 1200" role="img" aria-label="Rise As Captain">
    <defs>
      <linearGradient id="goldLetter" x1="0" y1="0" x2="1" y2="1">
        <stop offset="0" stop-color="var(--gold-light)"/>
        <stop offset="0.25" stop-color="#f8dca6"/>
        <stop offset="0.55" stop-color="var(--gold-mid)"/>
        <stop offset="0.78" stop-color="#f6de88"/>
        <stop offset="1" stop-color="var(--gold-deep)"/>
      </linearGradient>
    </defs>
    <g fill="url(#goldLetter)">
      <!-- line: RISE -->
      <text x="226" y="334" font-size="258" textLength="140" lengthAdjust="spacingAndGlyphs">R</text>
      <text x="366" y="334" font-size="258" textLength="70" lengthAdjust="spacingAndGlyphs">I</text>
      <text x="436" y="334" font-size="258" textLength="135" lengthAdjust="spacingAndGlyphs">S</text>
      <text x="571" y="334" font-size="258" textLength="130" lengthAdjust="spacingAndGlyphs">E</text>
      <!-- line: AS -->
      <text x="-2" y="717" font-size="534" textLength="470" lengthAdjust="spacingAndGlyphs">A</text>
      <text x="468" y="717" font-size="534" textLength="462" lengthAdjust="spacingAndGlyphs">S</text>
      <!-- line: CAPTAIN -->
      <text x="-17" y="959" font-size="330" textLength="150" lengthAdjust="spacingAndGlyphs">C</text>
      <text x="133" y="959" font-size="330" textLength="155" lengthAdjust="spacingAndGlyphs">A</text>
      <text x="288" y="959" font-size="330" textLength="140" lengthAdjust="spacingAndGlyphs">P</text>
      <text x="428" y="959" font-size="330" textLength="135" lengthAdjust="spacingAndGlyphs">T</text>
      <text x="563" y="959" font-size="330" textLength="155" lengthAdjust="spacingAndGlyphs">A</text>
      <text x="718" y="959" font-size="330" textLength="70" lengthAdjust="spacingAndGlyphs">I</text>
      <text x="788" y="959" font-size="330" textLength="155" lengthAdjust="spacingAndGlyphs">N</text>
    </g>
  </svg>

  <p class="cover__subtitle">The <span class="cover__numeral">10</span> Quiet Habits<br>of Remarkable Command</p>
</main>
</body>
</html>
```